Square graphic for social media post

I want to create a 1080 x 1080px all-black image for the quote below that I can share on social media. I want the emphasis to be primarily on the quote, secondarily on the portrait, and third (smallest) on the logo. I want the background on the portrait to be edited so it's transparent and just shows the face of the person on a black background (no brick wall visible).

Graphic color: black
Text color: white
Content: "What we went through is going to make the greatest generation of hoteliers our industry has ever seen." << biggest text
Dorian Welk << smaller text
President, Marrowgate Hotels << smaller text
[image of person - use whichever version looks better to you]
[Add Lodging Ledger logo - whichever looks better to you]

This image needs to be readable when sized down much smaller (400x400?) so want the text and portrait to take up most of the space.

I'd like the output both as PNG and original file (preferably Canva). Thanks!

Target Market(s)

Hotel managers

Industry/Entity Type

Hospitality

Font styles to use
Sans Serif

Colors

Designer to choose colors to be used in the design.

Requirements
Must have
• Needs to focus on the quote and the person quoted (the portrait)

```html
<!DOCTYPE html>
<html lang="en">
<head>
<meta charset="utf-8">
<title>Quote card – Dorian Welk</title>
<link href="https://fonts.googleapis.com/css2?family=Source+Serif+4:opsz,wght@8..60,400&family=Barlow:wght@500&display=swap" rel="stylesheet">
<style>
  :root {
    --ink: #000000;
    --paper: #ffffff;
    --portrait-top: #3b3f4a;
    --portrait-mid: #8a6f63;
    --portrait-low: #1f3a78;
  }
  * { margin: 0; padding: 0; box-sizing: border-box; }
  html, body {
    width: 1200px;
    height: 1200px;
    overflow: hidden;
    background: var(--ink);
  }
  .card {
    position: relative;
    width: 1200px;
    height: 1200px;
    background: var(--ink);
    color: var(--paper);
  }
  .card-frame {
    position: absolute;
    left: 41px;
    top: 41px;
    width: 1118px;
    height: 1118px;
    border: 2px solid var(--paper);
  }
  .quote {
    position: absolute;
    left: 106px;
    top: 98px;
    width: 1010px;
    font-family: "Source Serif 4", Georgia, serif;
    font-weight: 400;
    font-size: 81px;
    line-height: 98px;
    letter-spacing: 0.2px;
    white-space: nowrap;
  }
  .attribution {
    position: absolute;
    left: 0;
    top: 527px;
    width: 1200px;
    text-align: center;
    font-family: "Barlow", "Helvetica Neue", Arial, sans-serif;
    font-weight: 500;
    font-size: 30px;
    line-height: 52px;
    letter-spacing: 1.6px;
    text-transform: uppercase;
  }
  .portrait {
    position: absolute;
    left: 114px;
    top: 672px;
    width: 428px;
    height: 415px;
    background:
      radial-gradient(ellipse 42% 46% at 52% 40%, var(--portrait-mid) 0%, rgba(138,111,99,0.6) 55%, rgba(0,0,0,0) 100%),
      linear-gradient(180deg, var(--ink) 0%, var(--ink) 60%, var(--portrait-low) 80%, var(--portrait-low) 100%);
  }
  .publisher {
    position: absolute;
    left: 640px;
    top: 846px;
    width: 380px;
    text-align: center;
    font-family: "Barlow", "Helvetica Neue", Arial, sans-serif;
    font-weight: 500;
    font-size: 30px;
    letter-spacing: 6px;
    text-transform: uppercase;
  }
</style>
</head>
<body>
  <main class="card">
    <div class="card-frame"></div>

    <blockquote class="quote">"What we went through is<br>going to make the greatest<br>generation of hoteliers our<br>industry has ever seen."</blockquote>

    <p class="attribution">
      <span class="attribution-name">Dorian Welk</span><br>
      <span class="attribution-role">President, Marrowgate Hotels</span>
    </p>

    <div class="portrait" role="img" aria-label="Head-and-shoulders portrait of Dorian Welk, smiling, in a navy blazer and white shirt, on black"></div>

    <p class="publisher">Lodging Ledger</p>
  </main>
</body>
</html>
```